Local Pharmacy Drug Store looking for graphic store front design

Hello Everyone,
We are a local Pharmacy Drug Store looking for a Graphic Storefront design. We're a neighborhood pharmacy who serves all ages but serves a large portion of elderly patients.
I am attaching a image of the storefront (Sunpath store front.png), We are looking to have the whole right window side redesigned, so the majority of the work will happen there.
In regards to design I am attaching an example of what we are looking for (I.E Storefront Example.png). We want to have the name "Sunpath Pharmacy" Brightly displayed with words such as "Free Delivery" and "Most Insurance Accepted" included in smaller texts just like the example attached. We could also add images such as Vandry Network and a wheelchair. Be aware that we are looking for a design that has depth with color and background images. Please feel free to add any other context that would be fitting for a local neighborhood pharmacy.
Keep in mind that this design will only cover the right side window as shown in the "Sunpath Storefront" image

```html
<!DOCTYPE html>
<html lang="en">
<head>
<meta charset="utf-8">
<title>Sunpath Pharmacy – Window Poster</title>
<link rel="stylesheet" href="https://fonts.googleapis.com/css2?family=Montserrat:wght@500;700;800&display=swap">
<style>
  :root {
    --backdrop: #c9c9c9;
    --orange-deep: #ff7a00;
    --orange-mid: #ff9412;
    --orange-light: #ffb32e;
    --navy: #15197a;
    --white: #ffffff;
    --badge-blue: #1d3d7a;
    --badge-red: #f0552a;
  }
  * { margin: 0; padding: 0; box-sizing: border-box; }
  html, body { width: 851px; height: 1200px; overflow: hidden; }
  body {
    background: var(--backdrop);
    font-family: "Montserrat", sans-serif;
    position: relative;
  }
  .poster {
    position: absolute;
    left: 0; top: 101px;
    width: 851px; height: 998px;
    overflow: hidden;
    background:
      radial-gradient(ellipse 60% 45% at 50% 50%, var(--orange-light) 0%, rgba(255,179,46,0) 100%),
      linear-gradient(180deg, var(--orange-deep) 0%, var(--orange-mid) 55%, var(--orange-deep) 100%);
  }
  .brand-name {
    position: absolute; top: 78px; left: 0; width: 100%;
    text-align: center; color: var(--white);
    font-weight: 800; font-size: 84px; line-height: 1; letter-spacing: 1px;
  }
  .brand-tag {
    position: absolute; top: 182px; left: 0; width: 100%;
    text-align: center; color: var(--white);
    font-weight: 700; font-size: 44px; line-height: 1; letter-spacing: 22px;
    padding-left: 22px;
  }
  .wheelchair-art {
    position: absolute; left: 118px; top: 250px; width: 296px; height: 297px;
    border-radius: 50%;
    background: radial-gradient(circle at 55% 55%, #3a3a3a 0%, #6b6b6b 45%, rgba(255,160,40,0) 72%);
  }
  .divider {
    position: absolute; left: 454px; top: 275px; width: 2px; height: 247px;
    background: rgba(255,255,255,0.7);
  }
  .partner-badge {
    position: absolute; left: 491px; top: 324px; width: 236px; height: 146px;
    border-radius: 18px; border: 4px solid var(--white);
    background: var(--badge-blue);
    display: flex; flex-direction: column; align-items: center; justify-content: center;
    color: var(--white); font-weight: 800; font-size: 34px; line-height: 1.15; text-align: center;
  }
  .delivery-pill {
    position: absolute; left: 142px; top: 586px; width: 567px; height: 82px;
    border-radius: 41px; background: var(--navy);
    display: flex; align-items: center; padding-left: 18px;
  }
  .delivery-icon {
    width: 52px; height: 52px; border-radius: 50%; background: var(--white);
    flex: none; margin-right: 20px;
  }
  .delivery-text {
    font-weight: 800; font-size: 50px; line-height: 1; color: var(--white); letter-spacing: 0.5px;
  }
  .delivery-text .accent { color: var(--orange-mid); }
  .insurance-note {
    position: absolute; top: 676px; left: 0; width: 100%;
    text-align: center; color: var(--white);
    font-weight: 500; font-size: 37px; line-height: 1.1;
  }
  .pills-art {
    position: absolute; left: 0; bottom: 0; width: 100%; height: 253px;
    background: linear-gradient(180deg, rgba(255,255,255,0.35) 0%, #f28a1c 40%, #4aa8e0 100%);
    opacity: 0.85;
  }
</style>
</head>
<body>
  <main class="poster">
    <h1 class="brand-name">SUNPATH</h1>
    <p class="brand-tag">PHARMACY</p>

    <div class="wheelchair-art" role="img" aria-label="Illustration of a wheelchair"></div>
    <div class="divider"></div>
    <div class="partner-badge"><span>Vandry</span><span>Network</span></div>

    <div class="delivery-pill">
      <span class="delivery-icon"></span>
      <span class="delivery-text"><span class="accent">FREE</span> DELIVERY</span>
    </div>
    <p class="insurance-note">Most Insurance Accepted</p>

    <div class="pills-art" role="img" aria-label="Scattered colourful pills and capsules"></div>
  </main>
</body>
</html>
```